Business Card Design Project

I am a property development company requiring a professional looking business card.
The name of the my company is KLV SUMMITRA. I have attached a couple of designs that I have created on my own, that can give you an idea of what I am after.
Above the wording KLV SUMMITRA, I have a orange arc above these words to signify the sun is begining to rise above the horizon.
I have a few designs; Middle Rays, Side Rays, Horizontals Rays which are OK, but I am looking for the better design.
The Rear design of the card is what I had came up with. If you have a better design, I am happy to see it.
The design of the card can follow what I have came up with, or it can be totally different. The fonts needs to be adjusted to another font that is more suitable.
The colours that I have used is what I think I would like to stick with. As I have mentioned, the orange arc is to signify the sun rising. If you have a better colour scheme, I would consider it.
Looking at dealing with first home buyers and proffesional people.
Business

```html
<!DOCTYPE html>
<html lang="en">
<head>
<meta charset="utf-8">
<title>KLV SUMMITRA – Business Card</title>
<link rel="stylesheet" href="https://fonts.googleapis.com/css2?family=Questrial&family=Arimo:wght@400&family=Open+Sans:ital,wght@1,400;1,700&display=swap">
<style>
  :root {
    --backdrop: #d9d8d8;
    --card-dark: #141414;
    --card-dark-edge: #262626;
    --card-light: #efeeea;
    --sun-orange: #f3a21c;
    --ink: #111111;
    --paper-white: #f4f4f4;
  }
  * { margin: 0; padding: 0; box-sizing: border-box; }
  html, body {
    width: 1200px; height: 765px; overflow: hidden;
    background: var(--backdrop);
  }
  .canvas { position: relative; width: 1200px; height: 765px; }
  .card {
    position: absolute; top: 304px;
    width: 574px; height: 344px;
  }
  .card--front {
    left: 12px;
    background: linear-gradient(160deg, var(--card-dark-edge) 0%, var(--card-dark) 55%, #0b0b0b 100%);
    text-align: center;
  }
  .card--back { left: 615px; background: var(--card-light); }

  .brand-name {
    font-family: "Questrial", sans-serif;
    color: var(--sun-orange);
    letter-spacing: 0.04em;
    white-space: nowrap;
  }
  .brand-descriptor {
    font-family: "Questrial", sans-serif;
    color: var(--sun-orange);
    white-space: nowrap;
  }

  .card--front .brand-name {
    position: absolute; left: 0; right: 0; top: 140px;
    font-size: 38px; line-height: 1;
  }
  .card--front .brand-descriptor {
    position: absolute; left: 0; right: 0; top: 182px;
    font-size: 22px; line-height: 1;
  }
  .slogan {
    position: absolute; left: 0; right: 0; top: 228px;
    font-family: "Open Sans", sans-serif; font-style: italic;
    font-size: 19px; color: var(--paper-white);
  }

  .card--back .brand-block { position: absolute; left: 54px; top: 72px; text-align: center; }
  .card--back .brand-name { font-size: 20px; line-height: 1; }
  .card--back .brand-descriptor { font-size: 12.5px; margin-top: 3px; }

  .person-name {
    position: absolute; left: 53px; top: 126px;
    font-family: "Arimo", sans-serif; font-weight: 400;
    font-size: 32px; color: var(--ink);
    line-height: 1;
  }
  .person-role {
    position: absolute; left: 54px; top: 163px;
    font-family: "Open Sans", sans-serif; font-style: italic;
    font-size: 17px; letter-spacing: 0.32em; color: var(--ink);
  }
  .address {
    position: absolute; left: 54px; top: 197px;
    font-family: "Open Sans", sans-serif; font-style: italic;
    font-size: 13px; color: var(--ink);
  }
  .contact-list {
    position: absolute; left: 54px; top: 230px; list-style: none;
  }
  .contact-list li {
    display: flex; align-items: center; gap: 6px;
    height: 18px;
    font-family: "Open Sans", sans-serif; font-style: italic; font-weight: 700;
    font-size: 13.5px; color: var(--ink);
  }
  .contact-icon { width: 14px; height: 14px; flex: none; }
</style>
</head>
<body>
<main class="canvas">
  <section class="card card--front" aria-label="Card front">
    <div class="brand-name">KLV SUMMITRA</div>
    <div class="brand-descriptor">Property Developments</div>
    <p class="slogan">Rising with Trust, Care &amp; Commitment</p>
  </section>

  <section class="card card--back" aria-label="Card back">
    <div class="brand-block">
      <div class="brand-name">KLV SUMMITRA</div>
      <div class="brand-descriptor">Property Developments</div>
    </div>
    <h1 class="person-name">Marcus Webb</h1>
    <p class="person-role">Director</p>
    <p class="address">48 Ridgeway Street Kelvin NSW 2290 Australia</p>
    <ul class="contact-list">
      <li>
        <svg class="contact-icon" viewBox="0 0 14 14" aria-hidden="true">
          <rect width="14" height="14" rx="3" fill="#111"/>
          <path d="M3 5.5 Q7 2.5 11 5.5 L10 7 L8.5 6.2 L8.5 5.4 Q7 4.9 5.5 5.4 L5.5 6.2 L4 7 Z" fill="#fff"/>
          <rect x="4" y="7.5" width="6" height="3.5" rx="0.6" fill="#fff"/>
        </svg>
        0412 555 309
      </li>
      <li>
        <svg class="contact-icon" viewBox="0 0 14 14" aria-hidden="true">
          <rect width="14" height="14" rx="3" fill="#111"/>
          <rect x="3" y="4" width="8" height="6" fill="#fff"/>
          <path d="M3 4 L7 7.5 L11 4" fill="none" stroke="#111" stroke-width="0.9"/>
        </svg>
        marcus@klvsummitra.com.au
      </li>
      <li>
        <svg class="contact-icon" viewBox="0 0 14 14" aria-hidden="true">
          <rect width="14" height="14" rx="3" fill="#111"/>
          <circle cx="7" cy="7" r="4" fill="none" stroke="#fff" stroke-width="0.9"/>
          <ellipse cx="7" cy="7" rx="1.8" ry="4" fill="none" stroke="#fff" stroke-width="0.8"/>
          <path d="M3 7 H11 M3.6 5 H10.4 M3.6 9 H10.4" stroke="#fff" stroke-width="0.7"/>
        </svg>
        www.klvsummitra.com.au
      </li>
    </ul>
  </section>
</main>
</body>
</html>
```